Roland Pekkar Design, LLC (www.rolandpekkar.design)

A very hip, trendy architectural home page. Simple Menu upper right hand corner (About, Projects, Inspiration, Design-Build, Contact). In the "Projects" ... I want to click on each project and that will open up multiple photo's of that project. Attached are the graphics of my logo. I want the home page to be incredible ... I really market my name "Roland Pekkar" as sophisticated architecture. Colors/branding should be black/metallic/white/grey maybe with a pop of a bright color but not much. My architecture is like www.bravelinworkshop.com if you want to review as example. My specialty is industrial design, homes with architectural concrete design, steel beams, alot of glass. Very modern. My work is best illustrated at www.tervaquist.com.
Updates

Please see images uploaded in my brief. A new business card design by an AWESOME designer and some inspirational architectural projects I worked on.

Industry/Entity Type

Architecture

Coding

Coded - Design and coding required

Number of Pages Required

5+ page

Colors

Designer to choose only greyscale colors for use in the design.

Requirements
Must have
• The 1st project photo gallery is called "Raw Dwelling on the Gulf Edge"... Images of this project can be taken from: https://www.hobrentry.com/homedetails/2867-9th-Ave-NW-Naples-FL-34119/508314629_zpid/

The 2nd project photo gallery is called "Stone, Iron and Light Structures by the Quiet Bay". I will upload images for this project but use placeholder until I finalize.

The 3rd photo gallery is called "Early Sketches: Before the Build". I will forward pictures. for this.

Website should be easy to update and handover at completion as we will be updating frequently. Pagecraft, PLEM, or other type is fine as long as it looks profesional and high-class.
Nice to have
• Maybe the home page loads to just "Roland Pekkar Design, LLC ... Workshop for Bold Spatial Ideas" and has a click to enter button. Something cool maybe a fade it or something eye-catching and cool.
Should not have
• Should not be overly colorful.

```html
<!DOCTYPE html>
<html lang="en">
<head>
<meta charset="utf-8">
<title>Roland Pekkar Design, LLC — Website Pages</title>
<link href="https://fonts.googleapis.com/css2?family=Poppins:wght@400;500;600;700&family=Roboto:wght@300;400;500&display=swap" rel="stylesheet">
<style>
  :root{
    --board:#3b3b3b;
    --white:#ffffff;
    --ink:#1d1d1f;
    --text:#3a3a3a;
    --muted:#7a7a7a;
    --rule:#8d8d8d;
    --mist:#e8eaed;
    --footer:#1b1b1b;
    --black:#050505;
  }
  *{margin:0;padding:0;box-sizing:border-box}
  html,body{width:1200px;height:4000px;overflow:hidden}
  body{background:var(--board);font-family:"Roboto",sans-serif;color:var(--text);position:relative}
  .board-title{position:absolute;left:0;width:1200px;text-align:center;font-family:"Poppins",sans-serif;font-weight:600;font-size:31px;color:var(--white)}
  .panel{position:absolute;left:23px;width:1153px;overflow:hidden}

  /* header */
  .site-header{position:absolute;left:0;top:0;width:1153px;height:97px;z-index:2}
  .site-header.light{background:var(--white)}
  .brand{position:absolute;left:31px;top:30px;display:flex;align-items:center;gap:14px}
  .brand-box{width:36px;height:36px;border:2px solid currentColor}
  .brand-name{font-family:"Poppins",sans-serif;font-weight:500;font-size:17px;letter-spacing:1px}
  .nav{position:absolute;right:53px;top:40px;display:flex;gap:15px;font-size:10px;letter-spacing:1.6px;text-transform:uppercase}
  .nav a{text-decoration:none}
  .site-header.dark .brand{color:var(--white)}
  .site-header.dark .nav a{color:#b9bfca}
  .site-header.dark .nav a.active{color:var(--white)}
  .site-header.light .brand{color:var(--ink)}
  .site-header.light .nav a{color:var(--muted)}
  .site-header.light .nav a.active{color:var(--ink);font-weight:500}

  /* hero */
  .hero{top:115px;height:640px;
    background:
      linear-gradient(180deg,rgba(6,14,40,.55) 0%,rgba(6,14,40,.25) 45%,rgba(6,14,30,.35) 100%),
      radial-gradient(ellipse 260px 60px at 250px 430px,rgba(214,168,84,.55),rgba(214,168,84,0) 100%),
      radial-gradient(ellipse 300px 55px at 640px 440px,rgba(214,168,84,.45),rgba(214,168,84,0) 100%),
      radial-gradient(ellipse 120px 40px at 820px 410px,rgba(200,150,80,.35),rgba(200,150,80,0) 100%),
      linear-gradient(180deg,#0a1430 0%,#13224a 28%,#1c2a45 44%,#3a3d3f 56%,#4a4638 66%,#26401f 74%,#2e5026 86%,#1a2f14 100%)}
  .hero-title{position:absolute;left:0;width:1153px;top:278px;text-align:center;font-family:"Poppins",sans-serif;font-weight:600;font-size:25px;color:var(--white)}
  .hero-btn{position:absolute;left:513px;top:335px;width:129px;height:33px;border:1px solid var(--white);color:var(--white);font-size:9.5px;letter-spacing:1.8px;display:flex;align-items:center;justify-content:center;font-weight:500}

  /* projects page */
  .projects{top:860px;height:1912px;background:linear-gradient(180deg,var(--mist) 97px,#f3f4f6 700px,var(--white) 1300px)}
  .page-label{position:absolute;left:103px;font-weight:300;font-size:19px;letter-spacing:.5px;color:#555}
  .photo{position:absolute}
  .project-text{position:absolute;width:340px}
  .project-text.right{text-align:right}
  .year-line{display:flex;align-items:center;gap:12px;font-size:9.5px;color:var(--muted)}
  .year-line .rule{width:66px;height:1px;background:var(--rule)}
  .project-text.left .year-line{margin-left:-79px}
  .project-text.right .year-line{justify-content:flex-end;margin-right:-68px}
  .project-title{font-family:"Poppins",sans-serif;font-weight:500;font-size:19px;line-height:24px;color:var(--ink);margin-top:23px}
  .project-body{font-size:10.5px;line-height:27.5px;color:#444;margin-top:20px}
  .gallery-link{display:flex;align-items:center;gap:8px;font-size:9px;letter-spacing:.8px;color:#444;margin-top:12px}
  .project-text.right .gallery-link{justify-content:flex-end;margin-right:8px}

  .house-dusk{background:
      radial-gradient(ellipse 150px 40px at 45% 58%,rgba(255,206,110,.75),rgba(255,206,110,0) 100%),
      radial-gradient(ellipse 90px 30px at 20% 55%,rgba(255,196,100,.6),rgba(255,196,100,0) 100%),
      linear-gradient(172deg,rgba(0,0,0,0) 62%,rgba(150,150,230,.55) 66%,rgba(0,0,0,0) 72%),
      linear-gradient(180deg,#1a5ed0 0%,#4f8ee0 20%,#b9c6d8 34%,#8d8a80 44%,#6d6658 56%,#4a4a44 62%,#3f9a34 72%,#4cab3b 86%,#2f8a2a 100%)}
  .pavilion{background:
      radial-gradient(ellipse 200px 60px at 48% 50%,rgba(255,190,90,.7),rgba(255,190,90,0) 100%),
      radial-gradient(ellipse 60px 40px at 86% 55%,rgba(255,200,110,.5),rgba(255,200,110,0) 100%),
      linear-gradient(180deg,#3e78c8 0%,#5a86b8 12%,#1e2d22 26%,#2a3428 36%,#6b5234 48%,#54422f 62%,#3a2e25 72%,#8a3a2c 80%,#6a5a46 90%,#4a3f33 100%)}
  .loft{background:
      radial-gradient(ellipse 120px 90px at 78% 35%,rgba(235,232,222,.85),rgba(235,232,222,0) 100%),
      radial-gradient(ellipse 170px 45px at 45% 62%,rgba(226,220,206,.8),rgba(226,220,206,0) 100%),
      linear-gradient(180deg,#4a3a30 0%,#6e5646 25%,#7c6a58 45%,#5c4b3b 60%,#3f3126 78%,#2a211a 100%)}
  .restaurant{background:
      radial-gradient(ellipse 160px 50px at 60% 22%,rgba(230,180,110,.45),rgba(230,180,110,0) 100%),
      radial-gradient(ellipse 60px 120px at 12% 40%,rgba(70,90,55,.7),rgba(70,90,55,0) 100%),
      radial-gradient(ellipse 70px 110px at 62% 45%,rgba(70,95,55,.6),rgba(70,95,55,0) 100%),
      linear-gradient(180deg,#2a2823 0%,#3e3830 30%,#4a3f33 50%,#3a2c22 70%,#5a3a28 82%,#251d17 100%)}

  .footer-main{position:absolute;left:0;top:1777px;width:1153px;height:68px;background:var(--footer)}
  .footer-main .brand{left:93px;top:16px;color:var(--white)}
  .footer-main .brand-box{width:28px;height:28px}
  .footer-main .brand-name{font-size:14px}
  .footer-address{position:absolute;left:375px;width:400px;top:20px;text-align:center;font-size:10px;line-height:14px;letter-spacing:1.4px;color:#6f6f6f}
  .socials{position:absolute;left:958px;top:23px;display:flex;gap:8px}
  .socials span{border:1px solid #8a8a8a;color:#cfcfcf;font-size:8px;padding:4px 5px;letter-spacing:.5px}
  .footer-bottom{position:absolute;left:0;top:1845px;width:1153px;height:67px;background:var(--black);color:var(--white);font-size:9.5px;font-weight:500;text-align:center;line-height:67px;letter-spacing:.3px}

  /* detail page */
  .detail{top:2912px;height:1088px;background:linear-gradient(180deg,var(--mist) 97px,#f1f2f4 400px,#f6f6f6 800px)}
  .back-link{position:absolute;left:952px;top:138px;display:flex;align-items:center;gap:4px;font-size:9px;color:#555;letter-spacing:.5px}
  .detail-title{position:absolute;left:103px;top:170px;font-family:"Poppins",sans-serif;font-weight:500;font-size:20px;color:var(--ink)}
  .detail-desc{position:absolute;left:104px;top:205px;width:470px;font-size:10.5px;line-height:20px;color:#444}
  .detail-year{position:absolute;left:104px;top:258px;font-size:10.5px;color:#444}
  .bw-lounge{background:
      radial-gradient(ellipse 90px 50px at 55% 80%,#d8d8d8,rgba(216,216,216,0) 100%),
      linear-gradient(180deg,#2a2a2a 0%,#5a5a5a 22%,#9a9a9a 40%,#7a7a7a 58%,#bdbdbd 78%,#cfcfcf 100%)}
  .bw-atrium{background:
      radial-gradient(ellipse 100px 60px at 50% 12%,#e6e6e6,rgba(230,230,230,0) 100%),
      linear-gradient(180deg,#6a6a6a 0%,#9c9c9c 30%,#8a8a8a 55%,#b4b4b4 75%,#d4d4d4 100%)}
  .bw-kitchen{background:
      radial-gradient(ellipse 170px 30px at 50% 50%,#dcdcdc,rgba(220,220,220,0) 100%),
      linear-gradient(180deg,#4a4a4a 0%,#8c8c8c 25%,#bcbcbc 48%,#6a6a6a 66%,#a8a8a8 82%,#cacaca 100%)}
  .bw-corridor{background:
      radial-gradient(ellipse 40px 140px at 47% 50%,#ededed,rgba(237,237,237,0) 100%),
      linear-gradient(90deg,#d0d0d0 0%,#9a9a9a 20%,#5a5a5a 38%,#8a8a8a 50%,#3a3a3a 65%,#7a7a7a 82%,#b8b8b8 100%)}
  .bw-plain{background:linear-gradient(180deg,#3a3a3a 0%,#7a7a7a 60%,#9a9a9a 100%)}
  .fade{position:absolute;left:0;top:3835px;width:1200px;height:165px;background:linear-gradient(180deg,rgba(59,59,59,0) 0%,rgba(59,59,59,.85) 60%,var(--board) 100%)}
</style>
</head>
<body>

<div class="board-title" style="top:45px">Home Page</div>

<section class="panel hero" role="img" aria-label="Dusk photograph of a modern concrete and glass house with a lit interior and a wide lawn, under a dark blue overlay">
  <header class="site-header dark">
    <div class="brand"><div class="brand-box"></div><div class="brand-name">Roland Pekkar</div></div>
    <nav class="nav"><a class="active">Home</a><a>About</a><a>Projects</a><a>Inspiration</a><a>Design-Build</a><a>Contact</a></nav>
  </header>
  <h1 class="hero-title">Workshop for Bold Spatial Ideas</h1>
  <div class="hero-btn">EXPLORE IT</div>
</section>

<div class="board-title" style="top:791px">Projects Page</div>

<section class="panel projects">
  <header class="site-header light">
    <div class="brand"><div class="brand-box"></div><div class="brand-name">Roland Pekkar</div></div>
    <nav class="nav"><a>Home</a><a>About</a><a class="active">Projects</a><a>Inspiration</a><a>Design-Build</a><a>Contact</a></nav>
  </header>
  <div class="page-label" style="top:124px">PROJECTS</div>

  <div class="photo house-dusk" style="left:103px;top:165px;width:542px;height:335px" role="img" aria-label="Photograph of a concrete and glass house at dusk with a long reflecting pool and green lawn"></div>
  <div class="project-text left" style="left:701px;top:225px">
    <div class="year-line"><span class="rule"></span>2020</div>
    <div class="project-title">Raw Dwelling on the<br>Gulf Edge</div>
    <div class="project-body">Lorem Ipsum is simply dummy text of the printing and typesetting industry. Lorem Ipsum has been the industry's standard dummy text ever since the 1500s, when an unknown.</div>
    <div class="gallery-link">GALLERY <svg width="26" height="6" viewBox="0 0 26 6"><path d="M0 3H25M21 0.5L25 3L21 5.5" fill="none" stroke="#444" stroke-width="1"/></svg></div>
  </div>

  <div class="photo pavilion" style="left:496px;top:556px;width:542px;height:336px" role="img" aria-label="Photograph of a steel and glass pavilion house among tall pines with a glowing interior and wild grasses"></div>
  <div class="project-text right" style="left:98px;top:617px">
    <div class="year-line">2020<span class="rule"></span></div>
    <div class="project-title">Stone, Iron and Light Structures<br>by the Quiet Bay</div>
    <div class="project-body">Lorem Ipsum is simply dummy text of the printing and typesetting industry. Lorem Ipsum has been the industry's standard dummy text ever since the 1500s, when an unknown.</div>
    <div class="gallery-link">GALLERY <svg width="26" height="6" viewBox="0 0 26 6"><path d="M0 3H25M21 0.5L25 3L21 5.5" fill="none" stroke="#444" stroke-width="1"/></svg></div>
  </div>

  <div class="photo loft" style="left:103px;top:957px;width:542px;height:334px" role="img" aria-label="Photograph of an industrial loft living room with brick walls, pendant lamps and a linen sofa"></div>
  <div class="project-text left" style="left:701px;top:1017px">
    <div class="year-line"><span class="rule"></span>2020</div>
    <div class="project-title">Early Sketches:<br>Before the Build</div>
    <div class="project-body">Lorem Ipsum is simply dummy text of the printing and typesetting industry. Lorem Ipsum has been the industry's standard dummy text ever since the 1500s, when an unknown.</div>
    <div class="gallery-link">GALLERY <svg width="26" height="6" viewBox="0 0 26 6"><path d="M0 3H25M21 0.5L25 3L21 5.5" fill="none" stroke="#444" stroke-width="1"/></svg></div>
  </div>

  <div class="photo restaurant" style="left:496px;top:1351px;width:542px;height:336px" role="img" aria-label="Photograph of a dim restaurant interior with hanging bulbs, green plant walls and leather chairs"></div>
  <div class="project-text right" style="left:98px;top:1412px">
    <div class="year-line">2020<span class="rule"></span></div>
    <div class="project-title">Stone, Iron and Light Structures<br>by the Quiet Bay</div>
    <div class="project-body">Lorem Ipsum is simply dummy text of the printing and typesetting industry. Lorem Ipsum has been the industry's standard dummy text ever since the 1500s, when an unknown.</div>
    <div class="gallery-link">GALLERY <svg width="26" height="6" viewBox="0 0 26 6"><path d="M0 3H25M21 0.5L25 3L21 5.5" fill="none" stroke="#444" stroke-width="1"/></svg></div>
  </div>

  <footer>
    <div class="footer-main">
      <div class="brand"><div class="brand-box"></div><div class="brand-name">Roland Pekkar</div></div>
      <div class="footer-address">4180 Palmetto Grove Road Suite 512 Naples FL 34109<br>Call: 239.555.0148. Email: roland@rolandpekkar.design</div>
      <div class="socials"><span>Chirp</span><span>Facets</span><span>Pinboard</span></div>
    </div>
    <div class="footer-bottom">ROLAND PEKKAR DESIGN, LLC.&nbsp; 2021 ALL RIGHTS RESERVED</div>
  </footer>
</section>

<div class="board-title" style="top:2842px">Project Detail Page</div>

<section class="panel detail">
  <header class="site-header light">
    <div class="brand"><div class="brand-box"></div><div class="brand-name">Roland Pekkar</div></div>
    <nav class="nav"><a>Home</a><a>About</a><a class="active">Projects</a><a>Inspiration</a><a>Design-Build</a><a>Contact</a></nav>
  </header>
  <div class="page-label" style="top:126px">PROJECTS</div>
  <div class="back-link"><svg width="26" height="6" viewBox="0 0 26 6"><path d="M26 3H1M5 0.5L1 3L5 5.5" fill="none" stroke="#444" stroke-width="1"/></svg>BACK</div>
  <h2 class="detail-title">Raw Dwelling on the Gulf Edge</h2>
  <p class="detail-desc">Lorem Ipsum is simply dummy text of the printing and typesetting industry. Lorem Ipsum has been the industry's standard dummy text ever since the 1500s, when an unknown.</p>
  <div class="detail-year">Year 2020</div>

  <div class="photo bw-lounge" style="left:104px;top:327px;width:235px;height:304px" role="img" aria-label="Black and white photograph of an industrial interior with exposed ducts and lounge chairs"></div>
  <div class="photo house-dusk" style="left:362px;top:327px;width:384px;height:304px" role="img" aria-label="Color photograph of the concrete and glass house at dusk beside a reflecting pool"></div>
  <div class="photo bw-atrium" style="left:774px;top:327px;width:236px;height:304px" role="img" aria-label="Black and white photograph of a double-height room with steel trusses and a long table"></div>
  <div class="photo bw-kitchen" style="left:104px;top:651px;width:384px;height:303px" role="img" aria-label="Black and white photograph of an open kitchen with a long island and bar stools"></div>
  <div class="photo bw-corridor" style="left:511px;top:651px;width:499px;height:303px" role="img" aria-label="Black and white photograph of a glass-walled corridor with polished floors"></div>
  <div class="photo bw-plain" style="left:104px;top:978px;width:497px;height:110px" role="img" aria-label="Black and white photograph of another interior view"></div>
  <div class="photo bw-plain" style="left:626px;top:978px;width:384px;height:110px" role="img" aria-label="Black and white photograph of another exterior view"></div>
</section>
<div class="fade"></div>

</body>
</html>
```